Flyer for the Lumen 2025 Conference

I am looking to produce a flyer for our upcoming conference, Lumen 2025. This is an annual conference that we plan to publicize on social media. The ideal designer will create a flyer that is eye-catching and effectively communicates the key information. Please see attached our logo, speaker photo, and flyer content.

Target Market(s)

All demographics

Industry/Entity Type

Christian

Font styles to use
Sans Serif

Requirements
Should not have
• Cross, church

```html
<!DOCTYPE html>
<html lang="en">
<head>
<meta charset="UTF-8">
<title>Lumen 2025 Conference</title>
<link href="https://fonts.googleapis.com/css2?family=Cinzel:wght@400;500;700;800&family=Orbitron:wght@400&family=Lexend:wght@300;400;600;700&display=swap" rel="stylesheet">
<style>
  :root {
    --navy-deep: #041536;
    --navy: #072a6e;
    --royal: #0b4fc4;
    --bright: #1f7dff;
    --ice: #a9c8f5;
    --white: #ffffff;
    --orange: #f7941d;
    --sky-text: #3b8fff;
  }
  * { margin: 0; padding: 0; box-sizing: border-box; }
  html, body { width: 846px; height: 1200px; overflow: hidden; background: var(--navy-deep); }
  .flyer {
    position: relative; width: 846px; height: 1200px; overflow: hidden;
    font-family: "Lexend", sans-serif; color: var(--white);
    background:
      radial-gradient(ellipse 300px 280px at 520px 250px, rgba(31,125,255,0.55), transparent 70%),
      radial-gradient(ellipse 520px 420px at 423px 920px, rgba(11,79,196,0.45), transparent 75%),
      linear-gradient(180deg, #051a42 0%, #06276a 40%, #062a7a 70%, #04174a 100%);
  }
  .corner { position: absolute; border-color: var(--ice); border-style: solid; border-width: 0; }
  .corner--top { left: 34px; top: 34px; width: 145px; height: 145px; border-top-width: 2px; border-left-width: 2px; }
  .corner--bottom { left: 748px; top: 1002px; width: 59px; height: 159px; border-right-width: 2px; border-bottom-width: 2px; }

  .brand {
    position: absolute; right: 44px; top: 60px;
    display: flex; align-items: center; gap: 8px;
    font-weight: 600; font-size: 30px; letter-spacing: 1px; color: var(--white);
  }
  .brand__dot { width: 14px; height: 14px; border-radius: 50%; background: var(--orange); }

  .speaker-photo {
    position: absolute; left: 60px; top: 0; width: 600px; height: 760px;
    background:
      radial-gradient(ellipse 46% 50% at 50% 48%, rgba(28,110,225,0.85) 0%, rgba(18,88,205,0.55) 45%, rgba(10,60,160,0.2) 75%, transparent 100%);
  }

  .flare { position: absolute; top: 918px; width: 160px; height: 28px; }
  .flare--left { left: 0; background: radial-gradient(ellipse at 0% 50%, rgba(190,230,255,0.95), rgba(31,125,255,0.5) 35%, transparent 75%); }
  .flare--right { right: 0; background: radial-gradient(ellipse at 100% 50%, rgba(190,230,255,0.95), rgba(31,125,255,0.5) 35%, transparent 75%); }

  .title {
    position: absolute; left: 0; width: 846px; top: 562px; text-align: center;
    font-family: "Cinzel", serif; font-weight: 500; font-size: 98px; line-height: 1;
    color: var(--white); letter-spacing: -1px;
    text-shadow: 0 0 18px rgba(140,190,255,0.35);
  }
  .subtitle {
    position: absolute; left: 0; width: 846px; top: 676px; text-align: center;
    font-family: "Orbitron", sans-serif; font-size: 31px; letter-spacing: 2.5px; color: var(--orange);
  }

  .detail { position: absolute; top: 746px; width: 300px; text-align: center; }
  .detail--topic { left: 134px; }
  .detail--speaker { left: 415px; }
  .detail__label { font-size: 10px; letter-spacing: 3px; font-weight: 300; }
  .detail__value { margin-top: 8px; font-size: 21px; font-weight: 600; }
  .detail-divider { position: absolute; left: 425px; top: 745px; width: 1px; height: 46px; background: var(--ice); }

  .dates {
    position: absolute; left: 164px; top: 837px; width: 518px; height: 163px;
    border: 2px solid var(--ice); border-radius: 8px;
  }
  .dates__label { position: absolute; top: 9px; width: 100%; text-align: center; font-size: 8px; letter-spacing: 2px; }
  .date-card {
    position: absolute; top: 27px; width: 125px; height: 110px;
    border: 1.5px solid #5aa0ff; border-radius: 8px; text-align: center;
    background: linear-gradient(180deg, #1a6ae6 0%, #0d4fc8 55%, #0a3fa6 100%);
    box-shadow: 0 0 10px rgba(60,140,255,0.35);
  }
  .date-card:nth-of-type(1) { left: 40px; }
  .date-card:nth-of-type(2) { left: 196px; }
  .date-card:nth-of-type(3) { left: 351px; }
  .date-card__day { margin-top: 9px; font-size: 12.5px; font-weight: 300; }
  .date-card__num {
    font-family: "Cinzel", serif; font-weight: 800; font-size: 58px; line-height: 54px; margin-top: 0;
    text-shadow: 0 0 10px rgba(180,215,255,0.7), 0 2px 4px rgba(0,30,90,0.5);
  }
  .date-card__num sup { font-family: "Lexend", sans-serif; font-weight: 700; font-size: 19px; vertical-align: baseline; margin-left: 1px; text-shadow: none; }
  .date-card__time { margin-top: 5px; font-size: 10px; }

  .pin {
    position: absolute; left: 410px; top: 985px; width: 27px; height: 27px; border-radius: 50%;
    background: #e8f0ff; display: flex; align-items: center; justify-content: center;
  }

  .venue { position: absolute; left: 0; width: 846px; top: 1018px; text-align: center; font-size: 12.5px; line-height: 20px; }
  .venue__address { font-weight: 600; }

  .app-note {
    position: absolute; left: 120px; width: 606px; top: 1082px;
    display: flex; align-items: center; gap: 10px;
    font-size: 12.5px; letter-spacing: 1px; color: var(--sky-text); white-space: nowrap;
  }
  .app-note::before, .app-note::after { content: ""; flex: 1; height: 1px; background: rgba(169,200,245,0.35); }
  .app-note strong { color: var(--orange); font-weight: 700; }

  .contact { position: absolute; top: 1132px; display: flex; align-items: center; gap: 10px; }
  .contact--phone { left: 170px; }
  .contact--email { left: 339px; }
  .contact--web { left: 544px; }
  .contact__icon {
    width: 28px; height: 28px; border: 1.5px solid var(--white); border-radius: 50%;
    display: flex; align-items: center; justify-content: center;
  }
  .contact__label { font-size: 10.5px; font-weight: 300; }
  .contact__value { font-size: 12px; font-weight: 600; margin-top: 1px; }
</style>
</head>
<body>
<main class="flyer">
  <div class="corner corner--top"></div>
  <div class="corner corner--bottom"></div>

  <div class="speaker-photo" role="img" aria-label="Portrait photo of the speaker in a blue suit and glasses"></div>

  <div class="brand"><span class="brand__dot"></span>SELAH</div>

  <div class="flare flare--left"></div>
  <div class="flare flare--right"></div>

  <h1 class="title">LUMEN 2025</h1>
  <p class="subtitle">A PROPHETIC CONFERENCE</p>

  <div class="detail detail--topic">
    <p class="detail__label">TOPIC:</p>
    <p class="detail__value">The Voice Of The Lord</p>
  </div>
  <div class="detail-divider"></div>
  <div class="detail detail--speaker">
    <p class="detail__label">SPEAKER:</p>
    <p class="detail__value">Prophet Elias Marovo</p>
  </div>

  <section class="dates">
    <p class="dates__label">DATES</p>
    <div class="date-card">
      <p class="date-card__day">Friday, Dec</p>
      <p class="date-card__num">26<sup>th</sup></p>
      <p class="date-card__time">6:30PM - 9:00PM</p>
    </div>
    <div class="date-card">
      <p class="date-card__day">Saturday, Dec</p>
      <p class="date-card__num">27<sup>th</sup></p>
      <p class="date-card__time">5:30PM - 8:00PM</p>
    </div>
    <div class="date-card">
      <p class="date-card__day">Sunday, Dec</p>
      <p class="date-card__num">29<sup>th</sup></p>
      <p class="date-card__time">4:30PM - 7:00PM</p>
    </div>
  </section>

  <div class="pin">
    <svg width="12" height="14" viewBox="0 0 12 14" fill="none" stroke="#0a3fa6" stroke-width="1.5">
      <path d="M6 13s4.5-4.2 4.5-7.5a4.5 4.5 0 0 0-9 0C1.5 8.8 6 13 6 13z"/>
      <circle cx="6" cy="5.5" r="1.6"/>
    </svg>
  </div>

  <div class="venue">
    <p>The Harborview Performing Arts Center</p>
    <p class="venue__address">218 Millbrook Avenue Fairhaven, Maine 04011</p>
  </div>

  <p class="app-note"><span>DOWNLOAD <strong>THE SELAH APP</strong> TO STAY UPDATED ON THE EVENT</span></p>

  <div class="contact contact--phone">
    <span class="contact__icon">
      <svg width="14" height="14" viewBox="0 0 24 24" fill="none" stroke="#fff" stroke-width="2"><path d="M5 3h4l2 5-2.5 1.5a11 11 0 0 0 6 6L16 13l5 2v4a2 2 0 0 1-2 2A17 17 0 0 1 3 5a2 2 0 0 1 2-2z"/></svg>
    </span>
    <div><p class="contact__label">Phone:</p><p class="contact__value">207 555 0143</p></div>
  </div>
  <div class="contact contact--email">
    <span class="contact__icon">
      <svg width="14" height="14" viewBox="0 0 24 24" fill="none" stroke="#fff" stroke-width="2"><rect x="3" y="5" width="18" height="14" rx="2"/><path d="M3 7l9 6 9-6"/></svg>
    </span>
    <div><p class="contact__label">Email:</p><p class="contact__value">contact@selahvoice.org</p></div>
  </div>
  <div class="contact contact--web">
    <span class="contact__icon">
      <svg width="15" height="15" viewBox="0 0 24 24" fill="none" stroke="#fff" stroke-width="2"><circle cx="12" cy="12" r="9"/><path d="M3 12h18M12 3c3 3.5 3 14.5 0 18M12 3c-3 3.5-3 14.5 0 18"/></svg>
    </span>
    <div><p class="contact__label">Website:</p><p class="contact__value">www.selahvoice.org</p></div>
  </div>
</main>
</body>
</html>
```